Website for residential builder repair in Australia

I currently have my website setup using Servolink as hosting and started playing around with Wordpress.
I would like this to be able to be imported into Wordpress after built so I can add blog posts and edit site if needed.

I would like a website built that is simple and clear.

the main colours id like for the site are black and white and maybe grey.

I would like a simple welcome page, an about us page, a project page, and a blog page where I can write small articles.

will need to display licence number on website lic. 731046K

Target Market(s)

young to middle age families and couples looking to build a sustainable and high performance house.

Contact Information for Business Card

Tamsel Construction
Lic. 731046K (to be printed small)
email; bram@tamselconstruction.com.au
phone : 0428159067

Bram Keltoy - Director

Number of Pages Required

4 page

Font styles to use
Sans Serif
Other font styles liked:
• match logo

Colors

Designer to choose only greyscale colors for use in the design.

Requirements
Must have
• outline of works

Certified Passive House Tradesperson
New Builds
Renovations
Architectural homes
Nice to have
• thinking dark grey background or black

would like to see the logo embossed to look slightly 3d

back of card to be white or light grey so It can be written on.

letterhead to contain licence number swell

```html
<!DOCTYPE html>
<html lang="en">
<head>
<meta charset="utf-8">
<title>Tamsel Construction — Home</title>
<link href="https://fonts.googleapis.com/css2?family=Barlow:wght@400;500;600;700;800&family=Open+Sans:wght@400;600&display=swap" rel="stylesheet">
<style>
:root{
  --bg:#2c2c2c;
  --bg-dark:#222222;
  --bg-footer:#1d1d1d;
  --card:#383838;
  --accent:#e8e8e8;
  --accent-ink:#1a1a1a;
  --white:#ffffff;
  --text:#bdbdbd;
  --muted:#8a8a8a;
  --dot:#5a5a5a;
  --line:#444444;
}
*{margin:0;padding:0;box-sizing:border-box}
html,body{width:1200px;height:4100px;overflow:hidden}
body{background:var(--bg);font-family:"Open Sans",Arial,sans-serif;color:var(--text);position:relative}
h1,h2,h3,.nav,.btn,.brand{font-family:"Barlow",Arial,sans-serif}
.btn{display:inline-block;background:var(--accent);color:var(--accent-ink);font-weight:700;font-size:13px;letter-spacing:.5px;text-transform:uppercase;padding:9px 18px;text-decoration:none}
.btn-small{font-size:10px;padding:5px 10px}
.photo{position:absolute}

/* header */
.site-header{position:absolute;top:0;left:0;width:1200px;height:112px;background:var(--bg-dark);display:flex;align-items:center;padding:0 120px}
.brand{color:var(--white);font-weight:600;font-size:30px;letter-spacing:10px;line-height:1}
.brand small{display:block;font-size:10px;letter-spacing:6px;margin-top:6px;color:var(--muted)}
.nav{margin-left:auto;display:flex;gap:24px;align-items:center;font-size:13px;font-weight:600;text-transform:uppercase}
.nav a{color:var(--text);text-decoration:none}
.nav a.current{color:var(--white);border-bottom:2px solid var(--white);padding-bottom:2px}
.nav .btn{margin-left:14px;color:var(--accent-ink)}

/* hero */
.hero{position:absolute;top:112px;left:0;width:1200px;height:528px;background:linear-gradient(100deg,#c9c9c9 0%,#e6e6e6 30%,#f2f2f2 55%,#b3b3b3 78%,#616161 100%)}
.hero-copy{position:absolute;left:150px;top:160px}
.hero-copy h1{color:var(--white);font-size:34px;font-weight:800;text-transform:uppercase;line-height:1.2;text-shadow:0 2px 10px rgba(0,0,0,.55);margin-bottom:22px}
.hero-copy .btn{background:#2a2a2a;color:var(--white)}

/* section titles */
.section-title{position:absolute;left:0;width:1200px;text-align:center;color:var(--white);font-size:22px;font-weight:700;text-transform:uppercase;letter-spacing:1px}
.section-title::after{content:"";display:block;width:40px;height:2px;background:var(--text);margin:10px auto 0}

/* services */
.service{position:absolute;width:472px;height:356px}
.service-label{position:absolute;left:22px;bottom:22px}
.service-label h3{color:var(--white);font-size:20px;font-weight:800;text-transform:uppercase;line-height:1.15;text-shadow:0 2px 8px rgba(0,0,0,.6);margin-bottom:8px}

/* feature */
.feature-copy{position:absolute;left:640px;top:1625px;width:500px}
.feature-copy h2{color:var(--white);font-size:22px;font-weight:800;text-transform:uppercase;line-height:1.3;margin-bottom:20px}
.feature-copy p{font-size:13px;line-height:1.75;margin-bottom:22px}

/* testimonials */
.testimonial{position:absolute;top:2240px;width:440px;height:300px;background:var(--card);padding:34px 34px 30px 70px}
.testimonial .quote{position:absolute;left:26px;top:18px;font-family:Georgia,serif;font-size:54px;color:var(--muted)}
.testimonial p{font-size:13px;line-height:1.7;margin-bottom:40px}
.testimonial .who{color:var(--white);font-size:11px;font-weight:600;text-transform:uppercase}
.testimonial .where{font-size:11px;color:var(--muted)}
.arrow{position:absolute;top:2380px}
.dots{position:absolute;top:2580px;left:0;width:1200px;display:flex;justify-content:center;gap:10px}
.dots span{width:10px;height:10px;border-radius:50%;background:var(--dot)}
.dots span.on{background:var(--accent)}

/* portfolio */
.portfolio-item{position:absolute;top:2760px;width:376px;height:360px;border:6px solid #3a3a3a}
.portfolio-more{position:absolute;top:3170px;left:0;width:1200px;text-align:center}

/* cta */
.cta{position:absolute;top:3260px;left:0;width:1200px;height:480px;background:linear-gradient(90deg,#373737 0%,#c9c9c9 25%,#e6e6e6 50%,#9d9d9d 75%,#383838 100%)}
.cta-copy{position:absolute;top:170px;left:0;width:1200px;text-align:center}
.cta-copy h2{color:var(--white);font-size:34px;font-weight:800;text-transform:uppercase;line-height:1.15;text-shadow:0 2px 12px rgba(0,0,0,.7);margin-bottom:20px}
.cta-copy .btn{background:#2a2a2a;color:var(--white)}

/* footer */
.site-footer{position:absolute;top:3740px;left:0;width:1200px;height:360px;background:var(--bg-footer)}
.footer-brand{position:absolute;left:120px;top:90px;display:flex;align-items:center;gap:16px}
.footer-brand .mark{width:54px;height:54px;border-radius:50%;background:#9a9a9a}
.footer-brand .brand{font-size:24px;letter-spacing:5px}
.footer-col{position:absolute;top:40px}
.footer-col h3{color:var(--white);font-size:13px;font-weight:700;text-transform:uppercase;margin-bottom:16px}
.footer-col ul{list-style:none}
.footer-col li{font-size:12px;line-height:2;color:var(--text);text-transform:uppercase}
.contact-row{display:flex;align-items:center;gap:12px;margin-bottom:20px;font-size:11px;line-height:1.4}
.icon{width:28px;height:28px;border-radius:50%;background:#4a4a4a;display:flex;align-items:center;justify-content:center;flex:none}
.copyright{position:absolute;bottom:22px;left:0;width:1200px;text-align:center;font-size:10px;color:var(--muted)}
</style>
</head>
<body>

<header class="site-header">
  <div class="brand">TAMSEL<small>CONSTRUCTION</small></div>
  <nav class="nav">
    <a class="current" href="#">Home</a>
    <a href="#">About</a>
    <a href="#">Services</a>
    <a href="#">Portfolio</a>
    <a href="#">FAQ's</a>
    <a href="#">Contact</a>
    <a class="btn" href="#">Appointment</a>
  </nav>
</header>

<section class="hero" role="img" aria-label="Bright living room with large windows, white sofas and open shelving">
  <div class="hero-copy">
    <h1>The right windows &amp;<br>doors for you</h1>
    <a class="btn" href="#">Get free estimate</a>
  </div>
</section>

<h2 class="section-title" style="top:684px">Our Services</h2>

<article class="service" style="left:120px;top:780px;background:linear-gradient(135deg,#5e5e5e,#9a9a9a 50%,#555555)" role="img" aria-label="Tradesperson working on a timber window frame">
  <div class="service-label"><h3>Certified passive<br>house tradesperson</h3><a class="btn btn-small" href="#">Read more</a></div>
</article>
<article class="service" style="left:608px;top:780px;background:linear-gradient(160deg,#4a4a4a,#6a6a6a 45%,#7d7d7d)" role="img" aria-label="New two-storey home with lit windows at dusk">
  <div class="service-label"><h3>New builds</h3><a class="btn btn-small" href="#">Read more</a></div>
</article>
<article class="service" style="left:120px;top:1164px;background:linear-gradient(135deg,#6e6e6e,#cfcfcf 50%,#e3e3e3)" role="img" aria-label="Open interior under renovation with exposed brick wall">
  <div class="service-label"><h3>Renovations</h3><a class="btn btn-small" href="#">Read more</a></div>
</article>
<article class="service" style="left:608px;top:1164px;background:linear-gradient(170deg,#707070,#8e8e8e 40%,#3c3c3c 70%,#4a4a4a)" role="img" aria-label="Architectural home at sunset with lawn in front">
  <div class="service-label"><h3>Architectural homes</h3><a class="btn btn-small" href="#">Read more</a></div>
</article>

<div class="photo" style="left:0;top:1600px;width:600px;height:490px;background:linear-gradient(170deg,#a2a2a2,#5a5a5a 35%,#424242 65%,#555555)" role="img" aria-label="Weatherboard family home with gabled porch and garden path"></div>
<div class="feature-copy">
  <h2>Morbi accumsan ipsum velit. Nam nec tellus a odio tincidunt auctor amet mauris.</h2>
  <p>Proin gravida nibh vel velit auctor aliquet. Aenean sollicitudin, lorem quis bibendum auctor, nisi elit consequat ipsum, nec sagittis sem nibh id elit. Duis sed odio sit amet nibh vulputate cursus a sit amet mauris. Morbi accumsan ipsum velit. Nam nec tellus a odio tincidunt auctor a ornare odio. Sed non mauris vitae erat consequat auctor eu in elit. Class aptent taciti sociosqu ad litora torquent per conubia nostra.</p>
  <a class="btn btn-small" href="#">Read more</a>
</div>

<h2 class="section-title" style="top:2150px">Testimonials</h2>

<svg class="arrow" style="left:58px" width="16" height="24" viewBox="0 0 16 24"><path d="M12 2 L3 12 L12 22" stroke="#cfcfcf" stroke-width="3" fill="none"/></svg>
<svg class="arrow" style="left:1126px" width="16" height="24" viewBox="0 0 16 24"><path d="M4 2 L13 12 L4 22" stroke="#cfcfcf" stroke-width="3" fill="none"/></svg>

<blockquote class="testimonial" style="left:150px">
  <span class="quote">&ldquo;</span>
  <p>Homework but I hate carrots carrots consequat elit running from the start. Outdoor soccer team itself. That is, the earth is from the author of a football developers hate hate.</p>
  <div class="who">Liam Corvett</div>
  <div class="where">Geelong</div>
</blockquote>
<blockquote class="testimonial" style="left:610px">
  <span class="quote">&ldquo;</span>
  <p>Nibh pregnant microwave or outdoor author of bananas. Jasmine ride double, lorem auctor who drink unless semper nibh very pregnant.</p>
  <div class="who">Liam Corvett</div>
  <div class="where">Geelong</div>
</blockquote>

<div class="dots"><span class="on"></span><span class="on"></span><span class="on"></span><span></span></div>

<h2 class="section-title" style="top:2670px">Portfolio</h2>

<div class="portfolio-item" style="left:18px;background:linear-gradient(135deg,#2a2a2a,#5e5e5e 50%,#c2c2c2)" role="img" aria-label="Living area with tall steel-framed windows and timber floor"></div>
<div class="portfolio-item" style="left:412px;background:linear-gradient(180deg,#e2e2e2,#a6a6a6 60%,#555555)" role="img" aria-label="Carved armchair beside white French doors"></div>
<div class="portfolio-item" style="left:806px;background:linear-gradient(180deg,#cccccc,#ebebeb 45%,#2f2f2f)" role="img" aria-label="Dark-framed sliding doors opening onto a water view"></div>

<div class="portfolio-more"><a class="btn btn-small" href="#">View all portfolio</a></div>

<section class="cta" role="img" aria-label="Open-plan kitchen and lounge with leather sofa and pendant lights">
  <div class="cta-copy">
    <h2>Sleep in absolute peace wake<br>up to bright sunshine</h2>
    <a class="btn" href="#">Get free estimate</a>
  </div>
</section>

<footer class="site-footer">
  <div class="footer-brand"><span class="mark"></span><span class="brand">TAMSEL</span></div>

  <div class="footer-col" style="left:460px">
    <h3>Menu</h3>
    <ul><li>Home</li><li>About</li><li>Services</li><li>Portfolio</li><li>FAQ's</li><li>Contact</li></ul>
  </div>

  <div class="footer-col" style="left:670px">
    <h3>Contact us</h3>
    <div class="contact-row"><span class="icon"><svg width="14" height="14" viewBox="0 0 14 14"><path d="M7 1 C4.5 1 3 3 3 5 C3 8 7 13 7 13 C7 13 11 8 11 5 C11 3 9.5 1 7 1 Z" fill="#ddd"/><circle cx="7" cy="5" r="1.6" fill="#4a4a4a"/></svg></span><span>42 Rowan Street<br>Geelong VIC 3220</span></div>
    <div class="contact-row"><span class="icon"><svg width="14" height="14" viewBox="0 0 14 14"><path d="M3 1 L5.5 1 L6.5 4 L5 5.2 C5.8 7 7 8.2 8.8 9 L10 7.5 L13 8.5 L13 11 C13 12 12 13 11 13 C6 12.5 1.5 8 1 3 C1 2 2 1 3 1 Z" fill="#ddd"/></svg></span><span>Call us<br>0428159067</span></div>
    <div class="contact-row"><span class="icon"><svg width="14" height="14" viewBox="0 0 14 14"><rect x="1" y="3" width="12" height="8" fill="#ddd"/><path d="M1 3 L7 8 L13 3" stroke="#4a4a4a" stroke-width="1.2" fill="none"/></svg></span><span>E-mail us<br>bram@tamselconstruction.com.au</span></div>
  </div>

  <div class="footer-col" style="left:960px">
    <h3>Follow us</h3>
    <div class="contact-row"><span class="icon"></span><span>Like us on<br>our page</span></div>
    <div class="contact-row"><span class="icon"></span><span>Follow us on<br>our feed</span></div>
    <div class="contact-row"><span class="icon"></span><span>Connect on<br>our profile</span></div>
  </div>

  <div class="copyright">Copyright © 2024 All Rights Reserved · Lic. 731046K</div>
</footer>

</body>
</html>
```